out of the box Business Card Design for a Manufacturer / Distributor

We are a manufarturer and distributor of products.
the company name is VORTANI (Pic attached)

the picture is NOT a must have on the business Card.

the Business Card should look really professional and/or special, so out of the box thinking is welcome.

there should be 2 Adresses on the Business Card for Main and Branch Office.
Email Adress, homepage, Name is required
NO Phone Number

Our working field:
Private Labeling
high Quality Production
direct distribution
warehousing
trademark registration
legal support

Main Office:
Kornblumenweg 14
08352 Marlheim
Germany

Branch Office:
Daska Lane
Qasimpur
Pakistan

Names:
Lukas Feldhaus (Owner)
Imran Qureshi (Owner)

Email:
lukas@vortani-example.com
imran@vortani-example.com

homepage:
vortani-example.com

Industry/Entity Type

Manufacturer Distributer

Contact Information for Business Card

Vortani

Requirements
Must have
• Names, both office Adresses, email, homepage
Should not have
• Phone Number

```html
<!DOCTYPE html>
<html lang="en">
<head>
<meta charset="utf-8">
<title>Vortani Business Card</title>
<link href="https://fonts.googleapis.com/css2?family=Nunito+Sans:wght@400&family=PT+Sans:wght@400;700&display=swap" rel="stylesheet">
<style>
  :root {
    --ink: #000000;
    --paper: #ffffff;
    --page: #ffffff;
    --shadow: rgba(0,0,0,0.35);
  }
  * { margin: 0; padding: 0; box-sizing: border-box; }
  html, body { width: 1200px; height: 900px; overflow: hidden; background: var(--page); }
  body { position: relative; font-family: "PT Sans", sans-serif; color: var(--ink); }

  .card { position: absolute; width: 630px; height: 360px; box-shadow: 4px 6px 10px var(--shadow); overflow: hidden; }
  .card-front { left: 285px; top: 63px; background: var(--ink); }
  .card-back { left: 285px; top: 478px; background: var(--paper); }

  .front-name {
    position: absolute; left: 0; right: 0; top: 212px;
    text-align: center; color: var(--paper);
    font-family: "Nunito Sans", sans-serif; font-weight: 400;
    font-size: 52px; line-height: 1; letter-spacing: 0.5px;
  }

  .back-shapes { position: absolute; left: 0; top: 0; }

  .abs { position: absolute; }
  .brand { left: 100px; top: 46px; display: flex; align-items: center; gap: 10px; }
  .brand-dot { width: 28px; height: 28px; border-radius: 50%; background: var(--ink); }
  .brand-name { font-family: "Nunito Sans", sans-serif; font-size: 24px; line-height: 1; }
  .tagline { left: 100px; top: 101px; font-size: 9.5px; font-weight: 700; letter-spacing: 0.1px; }

  .services { left: 41px; top: 134px; display: grid; grid-template-columns: 135px 140px; row-gap: 2px; list-style: none; }
  .services li { font-size: 9.5px; font-weight: 700; line-height: 12px; display: flex; align-items: center; gap: 3px; white-space: nowrap; }
  .services li::before { content: ""; width: 8px; height: 8px; border-radius: 50%; background: var(--ink); flex: none; }

  .owner-icon { left: 326px; top: 73px; }
  .owners { left: 367px; top: 64px; }
  .owner-name { font-size: 25px; font-weight: 700; line-height: 25px; text-transform: uppercase; }
  .owner-role { font-size: 16px; margin-top: 12px; }

  .divider { left: 49px; top: 187px; width: 533px; height: 2px; background: var(--ink); }

  .contact-text { font-size: 15.5px; line-height: 21.5px; white-space: nowrap; font-style: normal; }
  .emails { left: 101px; top: 194px; }
  .web { left: 371px; top: 206px; }
  .addr-main { left: 100px; top: 246px; }
  .addr-branch { left: 371px; top: 246px; }

  .icon-mail { left: 65px; top: 209px; }
  .icon-globe { left: 334px; top: 203px; }
  .icon-pin-main { left: 64px; top: 266px; }
  .icon-pin-branch { left: 335px; top: 266px; }
</style>
</head>
<body>

  <section class="card card-front" aria-label="Card front">
    <h1 class="front-name">VORTANI</h1>
  </section>

  <section class="card card-back" aria-label="Card back">
    <svg class="back-shapes" width="630" height="360" viewBox="0 0 630 360" aria-hidden="true">
      <path d="M0 92 A34 34 0 0 1 34 126 L34 232 A34 34 0 0 1 0 266 Z" fill="var(--ink)"/>
      <path d="M630 92 A34 34 0 0 0 596 126 L596 232 A34 34 0 0 0 630 266 Z" fill="var(--ink)"/>
      <path d="M0 326 L303 326 C318 318 326 313 345 313 L630 313 L630 360 L0 360 Z" fill="var(--ink)"/>
    </svg>

    <div class="abs brand"><span class="brand-dot"></span><span class="brand-name">VORTANI</span></div>
    <p class="abs tagline">MANUFACTURER &amp; DISTRIBUTER</p>

    <ul class="abs services">
      <li>PRIVATE LABELING</li>
      <li>HIGH QUALITY PRODUCTION</li>
      <li>DIRECT DISTRIBUTION</li>
      <li>WAREHOUSING</li>
      <li>TRADEMARK REGISTRATION</li>
      <li>LEGAL SUPPORT</li>
    </ul>

    <svg class="abs owner-icon" width="28" height="37" viewBox="0 0 28 37" aria-hidden="true">
      <circle cx="14" cy="8" r="8" fill="var(--ink)"/>
      <path d="M2 19 H26 A2 2 0 0 1 28 21 V37 H0 V21 A2 2 0 0 1 2 19 Z" fill="var(--ink)"/>
    </svg>
    <div class="abs owners">
      <p class="owner-name">Lukas Feldhaus</p>
      <p class="owner-name">Imran Qureshi</p>
      <p class="owner-role">OWNERS</p>
    </div>

    <div class="abs divider"></div>

    <svg class="abs icon-mail" width="22" height="14" viewBox="0 0 22 14" aria-hidden="true">
      <rect x="1" y="1" width="20" height="12" fill="none" stroke="var(--ink)" stroke-width="2"/>
      <path d="M1 1 L11 8 L21 1" fill="none" stroke="var(--ink)" stroke-width="2"/>
    </svg>
    <div class="abs emails contact-text">
      <p>lukas@vortani-example.com</p>
      <p>imran@vortani-example.com</p>
    </div>

    <svg class="abs icon-globe" width="24" height="24" viewBox="0 0 24 24" aria-hidden="true">
      <g fill="none" stroke="var(--ink)" stroke-width="2">
        <circle cx="12" cy="12" r="11"/>
        <ellipse cx="12" cy="12" rx="5" ry="11"/>
        <line x1="12" y1="1" x2="12" y2="23"/>
        <line x1="1" y1="12" x2="23" y2="12"/>
        <path d="M3 6.5 H21 M3 17.5 H21"/>
      </g>
    </svg>
    <p class="abs web contact-text">www.vortani-example.com</p>

    <svg class="abs icon-pin-main" width="22" height="24" viewBox="0 0 22 24" aria-hidden="true">
      <path d="M11 23 L4 15.5 A9.5 9.5 0 1 1 18 15.5 Z" fill="none" stroke="var(--ink)" stroke-width="2.2" stroke-linejoin="round"/>
      <circle cx="11" cy="9" r="4" fill="none" stroke="var(--ink)" stroke-width="2.2"/>
    </svg>
    <address class="abs addr-main contact-text">
      Kornblumenweg 14<br>08352 Marlheim<br>Germany&nbsp; (MAIN OFFICE)
    </address>

    <svg class="abs icon-pin-branch" width="22" height="24" viewBox="0 0 22 24" aria-hidden="true">
      <path d="M11 23 L4 15.5 A9.5 9.5 0 1 1 18 15.5 Z" fill="none" stroke="var(--ink)" stroke-width="2.2" stroke-linejoin="round"/>
      <circle cx="11" cy="9" r="4" fill="none" stroke="var(--ink)" stroke-width="2.2"/>
    </svg>
    <address class="abs addr-branch contact-text">
      Daska Lane<br>Qasimpur<br>Pakistan&nbsp; (BRANCH OFFICE)
    </address>
  </section>

</body>
</html>
```